New Business Card Design Project

Looking for a modern business card design for an import distribution business for industrial technical products. The winning design will translate modern, sophistication, technical, professional and sustainable.

Target Market(s)

Technical customers

Industry/Entity Type

Business

Contact Information for Business Card

Dean Hollis
Sales Manager
M: 0461 752 918
P: 1300 817 294
dean@quorvelindustrial.com.au
4/81 Harcourt Vale Road
Seven Hills NSW 2147
www.quorvelindustrial.com.au

Font styles to use
Sans Serif

Colors
ec1f27
606060
000000
fbfbfb

Requirements
Must have
• My Logo which is the Quorvel Industrial logo attached
Nice to have
• Eurostile Bold font

```html
<!DOCTYPE html>
<html lang="en">
<head>
<meta charset="utf-8">
<title>Quorvel Industrial — Business Card</title>
<link href="https://fonts.googleapis.com/css2?family=Roboto:wght@400;500;700&display=swap" rel="stylesheet">
<style>
  :root {
    --red: #ec1f27;
    --card-red: #d9423a;
    --grey: #606060;
    --slate: #6b6f76;
    --slate-light: #a9abb0;
    --black: #141414;
    --paper: #fbfbfb;
    --stage: #e6e6e6;
  }
  * { box-sizing: border-box; margin: 0; padding: 0; }
  html, body {
    width: 1200px; height: 726px; overflow: hidden;
    background: var(--stage);
    font-family: "Roboto", Arial, sans-serif;
  }
  .canvas {
    width: 1200px; height: 726px;
    display: flex; align-items: center; justify-content: center; gap: 60px;
  }
  .card {
    position: relative;
    width: 520px; height: 318px;
    overflow: hidden;
    box-shadow: 0 6px 18px rgba(0,0,0,0.18);
  }
  .card-back { background: var(--black); display: flex; align-items: center; justify-content: center; }
  .card-front { background: var(--paper); }
  .wordmark { display: flex; align-items: center; gap: 12px; }
  .wordmark-square { width: 34px; height: 34px; background: var(--red); }
  .wordmark-name {
    font-weight: 700; font-size: 30px; letter-spacing: 1px;
    color: var(--red); text-transform: uppercase; line-height: 1;
  }
  .card-back .wordmark-name { font-size: 34px; }
  .card-back .wordmark-square { width: 40px; height: 40px; }
  .card-front .wordmark { position: absolute; top: 34px; right: 30px; }
  .card-front .wordmark-name { font-size: 22px; }
  .card-front .wordmark-square { width: 26px; height: 26px; }
  .swoosh { position: absolute; inset: 0; }
  .person { position: absolute; left: 30px; top: 112px; }
  .person-name { font-size: 20px; font-weight: 700; color: var(--grey); }
  .person-role { font-size: 11px; color: var(--grey); margin-top: 3px; }
  .contact-list { position: absolute; left: 30px; top: 180px; list-style: none; }
  .contact-list li {
    display: flex; align-items: center; gap: 8px;
    font-size: 12px; color: var(--grey); line-height: 20px;
  }
  .contact-list svg { width: 11px; height: 11px; fill: var(--red); flex: none; }
  .address {
    position: absolute; right: 24px; top: 232px;
    text-align: right; color: #fff; font-size: 12px; line-height: 18px;
    font-style: normal;
  }
</style>
</head>
<body>
<main class="canvas">
  <section class="card card-back" aria-label="Card back">
    <div class="wordmark">
      <span class="wordmark-square"></span>
      <span class="wordmark-name">Quorvel Industrial</span>
    </div>
  </section>

  <section class="card card-front" aria-label="Card front">
    <svg class="swoosh" viewBox="0 0 520 318" aria-hidden="true">
      <path d="M520 90 C460 112 420 162 370 200 C330 240 270 290 200 318 L520 318 Z" fill="var(--card-red)"/>
      <path d="M520 74 C455 96 410 150 358 188 C310 230 240 280 150 318 L172 318 C250 284 318 236 364 196 C416 156 462 104 520 86 Z" fill="var(--slate)"/>
      <path d="M520 58 C452 80 404 130 350 172 C300 212 250 240 210 256 C258 242 306 216 356 180 C410 140 456 88 520 66 Z" fill="var(--slate-light)"/>
    </svg>

    <div class="wordmark">
      <span class="wordmark-square"></span>
      <span class="wordmark-name">Quorvel Industrial</span>
    </div>

    <div class="person">
      <p class="person-name">Dean Hollis</p>
      <p class="person-role">Sales Manager</p>
    </div>

    <ul class="contact-list">
      <li><svg viewBox="0 0 12 12"><rect x="3" y="0" width="6" height="12" rx="1.2"/></svg>0461 752 918</li>
      <li><svg viewBox="0 0 12 12"><path d="M1 3 Q6 0 11 3 L10 5 L8 4 L8 6 L11 8 L11 12 L1 12 L1 8 L4 6 L4 4 L2 5 Z"/></svg>1300 817 294</li>
      <li><svg viewBox="0 0 12 12"><path d="M0 2 H12 V10 H0 Z M0 2 L6 7 L12 2" stroke="#fff" stroke-width="1"/></svg>dean@quorvelindustrial.com.au</li>
      <li><svg viewBox="0 0 12 12"><circle cx="6" cy="6" r="6"/></svg>www.quorvelindustrial.com.au</li>
    </ul>

    <address class="address">
      4/81 Harcourt Vale Road<br>Seven Hills NSW 2147
    </address>
  </section>
</main>
</body>
</html>
```